TASMANOVA IT SUPPORT WEBSITE AND CODING

We are a small IT Support company based if Broome Western Australia, we need to have our existing website www.tasmanova.com.au converted or redesigned to a format that can be read on iphone , ipad and all browsers, must have facebook like button.

THIS PROJECT IS FOR DESIGN AND CODING OF COMPLETE WEBSITE.

Target Market(s)

Broome Local Businesses and Public.

Industry/Entity Type

It Company

Requirements
Must have
• Must be able to be viewed on all mobile devices , iphone , ipad , must have a facebook like button, the logo for tasmanovA is the way tasman ova is written in orange on the current website which is used on all our advertising which needs to stay the same or only change slightly.
Nice to have
• Contact us page that emails us.
Our address on a map.

```html
<!DOCTYPE html>
<html lang="en">
<head>
<meta charset="utf-8">
<title>tasmanovA – IT Support</title>
<link rel="stylesheet" href="https://fonts.googleapis.com/css2?family=Open+Sans:wght@400;600&family=Arimo:ital,wght@0,400;0,700;1,400;1,700&display=swap">
<style>
  :root {
    --orange: #e8502e;
    --navy: #1d3f86;
    --nav-band: #d7e7f7;
    --nav-line: #a9bfd6;
    --page-pink: #f6e0e0;
    --body-text: #333333;
    --panel: #7b5e66;
    --panel-head: #8f747b;
    --white: #ffffff;
    --footer-text: #3a3a3a;
    --muted: #666666;
  }
  * { margin: 0; padding: 0; box-sizing: border-box; }
  html, body { width: 838px; height: 1200px; overflow: hidden; }
  body {
    position: relative;
    background: var(--page-pink);
    font-family: "Arimo", Arial, sans-serif;
    color: var(--body-text);
  }
  .abs { position: absolute; }

  /* Header */
  .site-header { position: absolute; left: 0; top: 0; width: 838px; height: 108px; background: var(--white); }
  .brand { left: 36px; top: 18px; font-family: "Open Sans", sans-serif; font-size: 38px; font-weight: 400; color: var(--orange); letter-spacing: 0.5px; }
  .socialize { left: 651px; top: 29px; font-family: "Open Sans", sans-serif; font-size: 11px; color: #222; }
  .social-dot { top: 26px; width: 17px; height: 17px; border-radius: 50%; background: #9aa6b8; }
  .live-chat { left: 582px; top: 66px; font-family: "Open Sans", sans-serif; font-size: 14px; color: #111; }
  .phone-number { left: 714px; top: 62px; font-family: "Open Sans", sans-serif; font-size: 17px; color: #111; }

  /* Navigation */
  .main-nav { position: absolute; left: 0; top: 108px; width: 838px; height: 52px; background: var(--nav-band); border-bottom: 1px solid var(--nav-line); }
  .nav-item { top: 12px; font-family: "Open Sans", sans-serif; font-size: 18px; color: var(--orange); }
  .nav-item.active { left: 27px; top: 7px; width: 78px; height: 34px; line-height: 34px; text-align: center; border-radius: 17px; background: var(--navy); color: var(--white); }

  /* Hero */
  .hero { position: absolute; left: 0; top: 181px; width: 838px; height: 356px;
    background: linear-gradient(100deg, #6d4a2c 0%, #a57b52 30%, #c9a582 55%, #8e7a78 80%, #b59a7d 100%);
    box-shadow: 0 3px 6px rgba(0,0,0,0.25); }
  .hero-title { left: 15px; top: 60px; font-family: "Open Sans", sans-serif; font-size: 38px; font-weight: 400; line-height: 47px; color: var(--white); }
  .hero-title em { font-style: normal; color: var(--orange); }
  .slider-dot { top: 321px; width: 14px; height: 14px; border-radius: 50%; background: #e6e6e6; }
  .slider-dot.current { background: #8c96c4; }

  /* Main content */
  .section-title { left: 14px; font-family: "Open Sans", sans-serif; font-size: 22px; font-weight: 400; color: var(--orange); }
  .copy { left: 21px; width: 500px; font-size: 10.6px; line-height: 13.5px; }
  .signature { left: 21px; font-size: 10.6px; font-weight: 700; }

  /* Sidebar panels */
  .panel { left: 557px; width: 265px; height: 176px; border-radius: 6px; background: var(--panel); }
  .panel-head { position: absolute; left: 16px; top: 8px; width: 235px; height: 30px; border-radius: 4px; background: var(--panel-head); border: 1px solid #b29ca2; }
  .panel-icon { position: absolute; left: 14px; top: 8px; width: 22px; height: 13px; border-radius: 7px; background: #d9d9d9; }
  .panel-title { position: absolute; left: 53px; top: 5px; font-family: "Open Sans", sans-serif; font-size: 14px; color: var(--white); }
  .panel-item { position: absolute; left: 20px; width: 235px; font-size: 10.6px; line-height: 13.5px; color: var(--white); }
  .panel-more { position: absolute; right: 24px; bottom: 8px; font-size: 10px; font-style: italic; font-weight: 700; color: #d8c8cc; }

  /* Footer */
  .site-footer { position: absolute; left: 0; top: 1025px; width: 838px; height: 175px; background: var(--white); border-top: 1px solid #e0d0d0; }
  .foot-col { top: 16px; font-size: 10.6px; line-height: 15px; color: var(--footer-text); }
  .foot-about { left: 129px; width: 195px; font-size: 10.2px; letter-spacing: -0.1px; }
  .foot-more { left: 233px; top: 97px; font-size: 10px; font-style: italic; font-weight: 700; color: #111; }
  .foot-map { left: 610px; top: 18px; width: 213px; height: 94px; background: linear-gradient(135deg, #e4e4e0 0%, #d8dbd6 60%, #b7c9d6 100%); }
  .copyright { left: 0; top: 138px; width: 838px; text-align: center; font-size: 10.6px; font-style: italic; color: var(--muted); }
</style>
</head>
<body>

<header class="site-header">
  <div class="abs brand">tasmanovA</div>
  <div class="abs socialize">SOCIALIZE WITH US</div>
  <span class="abs social-dot" style="left:757px"></span>
  <span class="abs social-dot" style="left:781px"></span>
  <span class="abs social-dot" style="left:806px"></span>

  <svg class="abs" style="left:550px;top:65px" width="24" height="22" viewBox="0 0 24 22" aria-hidden="true">
    <rect x="1" y="1" width="22" height="15" rx="3" fill="#3f86d8"/>
    <path d="M6 15 L6 21 L12 15 Z" fill="#3f86d8"/>
  </svg>
  <div class="abs live-chat">LIVE CHAT</div>

  <svg class="abs" style="left:683px;top:62px" width="22" height="22" viewBox="0 0 22 22" aria-hidden="true">
    <circle cx="11" cy="11" r="10" fill="#2c6fc8"/>
    <path d="M8 6 C6 8 7 12 10 15 C12 17 14 17 15 16 L13.5 13.5 L12 14 C10.5 13 9 11.5 8.5 10 L9.5 8.8 Z" fill="#fff"/>
  </svg>
  <div class="abs phone-number">100-37-51620</div>
</header>

<nav class="main-nav">
  <a class="abs nav-item active">HOME</a>
  <a class="abs nav-item" style="left:134px">ABOUT US</a>
  <a class="abs nav-item" style="left:257px">SERVICES</a>
  <a class="abs nav-item" style="left:376px">PRICES</a>
  <a class="abs nav-item" style="left:475px">CONTACTS</a>
</nav>

<section class="hero" role="img" aria-label="Photo of a smiling family gathered around a laptop in a warm wooden kitchen">
  <h1 class="abs hero-title">The <em>Experience</em><br>you need<br>and the <em>quality</em><br>you deserve</h1>
  <span class="abs slider-dot" style="left:393px"></span>
  <span class="abs slider-dot current" style="left:412px"></span>
  <span class="abs slider-dot" style="left:431px"></span>
</section>

<main>
  <h2 class="abs section-title" style="top:583px">WELCOME TO OUR SITE</h2>
  <p class="abs copy" style="top:623px">Lorem Ipsum is simply dummy text of the printing and typesetting industry. Lorem Ipsum has been the industry's standard dummy text ever since the 1500s, when an unknown printer took a galley of type and scrambled it to make a type specimen book. It has survived not only five centuries, but also the leap into electronic typesetting, remaining essentially unchanged. It was popularised in the 1960s with the release of Typeline sheets containing Lorem Ipsum passages, and more recently with desktop publishing software like Pressmark Layout including versions of Lorem Ipsum.</p>
  <p class="abs copy" style="top:717px">Lorem Ipsum is simply dummy text of the printing and typesetting industry. Lorem Ipsum has been the industry's standard dummy text ever since the 1500s, when an unknown printer took a galley of type and scrambled it to make a type specimen book. It has survived not only five centuries, but also the leap into electronic typesetting, remaining essentially unchanged. It was popularised in the 1960s with the release of Typeline sheets containing Lorem Ipsum passages, and more recently with desktop publishing software like Pressmark Layout including versions of Lorem Ipsum.</p>

  <h2 class="abs section-title" style="top:813px">TESTIMONIAL</h2>
  <p class="abs copy" style="top:849px">Lorem Ipsum is simply dummy text of the printing and typesetting industry. Lorem Ipsum has been the industry's standard dummy text ever since the 1500s, when an unknown printer took a galley of type and scrambled it to make a type specimen book.</p>
  <p class="abs signature" style="top:903px">Laurence .MD Y company</p>
  <p class="abs copy" style="top:930px">Lorem Ipsum is simply dummy text of the printing and typesetting industry. Lorem Ipsum has been the industry's standard dummy text ever since the 1500s, when an unknown printer took a galley of type and scrambled it to make a type specimen book.</p>
  <p class="abs signature" style="top:984px">Tamsin Y - Student</p>
</main>

<aside>
  <div class="abs panel" style="top:569px">
    <div class="panel-head"><span class="panel-icon"></span><span class="panel-title">BEST SERVICES</span></div>
    <p class="panel-item" style="top:51px">Lorem Ipsum is simply dummy text of the printing and typesetting industry.</p>
    <p class="panel-item" style="top:88px">Lorem Ipsum is simply dummy text of the printing and typesetting industry.</p>
    <p class="panel-item" style="top:125px">Lorem Ipsum is simply dummy text of the printing and typesetting industry.</p>
    <span class="panel-more">VIEW MORE&gt;&gt;&gt;</span>
  </div>
  <div class="abs panel" style="top:758px">
    <div class="panel-head"><span class="panel-icon"></span><span class="panel-title">LATEST NEWS</span></div>
    <p class="panel-item" style="top:55px">Lorem Ipsum is simply dummy text of the printing and typesetting industry.</p>
    <p class="panel-item" style="top:91px">Lorem Ipsum is simply dummy text of the printing and typesetting industry.</p>
    <p class="panel-item" style="top:127px">Lorem Ipsum is simply dummy text of the printing and typesetting industry.</p>
    <span class="panel-more">VIEW MORE&gt;&gt;&gt;</span>
  </div>
</aside>

<footer class="site-footer">
  <div class="abs foot-col" style="left:21px">About Us<br>Customer Service<br>Site Map<br>Orders and Returns<br>Contact US</div>
  <div class="abs foot-col foot-about">Contrary to popular belief, Lorem Ipsum<br>is not simply random text. It has roots in<br>a piece of classical Latin literature from<br>45 BC, making it over 2000 years old.<br>Daniel Hartwell,rom a Lorem Ipsum.</div>
  <div class="abs foot-more">VIEW MORE&gt;&gt;&gt;</div>
  <div class="abs foot-col" style="left:351px">Shipping &amp; returns<br>Secure Shopping<br>Affiliates<br>Sales</div>
  <div class="abs foot-col" style="left:480px">Tasman Ova.<br>PO BOX 4180<br>KELLAWAY WA<br><span style="display:block;margin-top:4px">TELEPHONE:</span>+91 947 30612</div>
  <div class="abs foot-map" role="img" aria-label="Street map showing the office location"></div>
  <div class="abs copyright">Copyright @ 2012 All Rights Reserved</div>
</footer>

</body>
</html>
```